Torvelin Business Card

We need a business card design. We have a logo from a previous PixelHarbor project and I am attaching the logo files in jpeg and photoshop.

Business

```html
<!DOCTYPE html>
<html lang="en">
<head>
<meta charset="utf-8">
<title>Torvelin Business Card</title>
<link rel="stylesheet" href="https://fonts.googleapis.com/css2?family=Open+Sans:wght@400;600;700&family=Oswald:wght@600&display=swap">
<style>
  :root {
    --page: #e6e6e6;
    --card: #3b3c3d;
    --card-edge: #333435;
    --green: #5cc21c;
    --green-dark: #2f6b0c;
    --text: #f2f2f2;
    --muted: #bdbdbd;
  }
  * { box-sizing: border-box; margin: 0; padding: 0; }
  html, body {
    width: 1200px; height: 900px; overflow: hidden;
    background: var(--page);
    font-family: "Open Sans", Arial, sans-serif;
  }
  .card {
    position: absolute; left: 270px;
    width: 660px; height: 377px;
    background: var(--card);
    border: 1px solid var(--card-edge);
    box-shadow: 0 10px 28px rgba(0,0,0,.22);
    overflow: hidden;
  }
  .card--back { top: 50px; }
  .card--front { top: 473px; }

  .wordmark {
    font-family: "Open Sans", Arial, sans-serif;
    font-weight: 700; color: var(--green);
    letter-spacing: -0.5px;
    display: flex; align-items: center; gap: 12px;
  }
  .wordmark__square { width: 0.8em; height: 0.8em; background: var(--green); }

  /* back */
  .back__logo {
    position: absolute; left: 0; right: 0; top: 130px;
    justify-content: center; font-size: 62px;
  }
  .back__rule { position: absolute; left: 175px; width: 270px; height: 5px; background: var(--green); }
  .back__rule--a { top: 240px; }
  .back__rule--b { top: 252px; }
  .back__stripe { position: absolute; top: 0; bottom: 0; width: 5px; background: var(--green); }
  .back__stripe--a { left: 588px; }
  .back__stripe--b { left: 602px; }

  /* front */
  .front__rule { position: absolute; height: 5px; background: var(--green); }
  .front__rule--top-a { left: 150px; top: 22px; width: 190px; }
  .front__rule--top-b { left: 150px; top: 34px; width: 190px; }
  .front__rule--bottom-a { left: 515px; top: 336px; width: 145px; }
  .front__rule--bottom-b { left: 515px; top: 348px; width: 145px; }

  .person { position: absolute; left: 330px; top: 62px; color: var(--text); }
  .person__name {
    font-family: "Oswald", Impact, sans-serif; font-weight: 600;
    font-size: 30px; letter-spacing: 0.5px; line-height: 1;
  }
  .person__title { font-size: 9px; letter-spacing: 3px; color: var(--muted); margin-top: 6px; }

  .contact { position: absolute; left: 34px; top: 120px; list-style: none; color: var(--text); }
  .contact__item { display: flex; align-items: center; gap: 10px; height: 30px; font-size: 14px; }
  .contact__item--phone { font-size: 19px; }
  .icon {
    width: 20px; height: 20px; border-radius: 50%;
    background: var(--green); flex: none;
    display: flex; align-items: center; justify-content: center;
  }

  .front__logo { position: absolute; left: 395px; top: 236px; font-size: 48px; }

  .website {
    position: absolute; left: 300px; top: 306px;
    display: flex; align-items: center; gap: 12px;
    color: var(--text); font-size: 14px;
  }
</style>
</head>
<body>

<section class="card card--back" aria-label="Card back">
  <div class="wordmark back__logo"><span class="wordmark__square"></span>Torvelin</div>
  <div class="back__rule back__rule--a"></div>
  <div class="back__rule back__rule--b"></div>
  <div class="back__stripe back__stripe--a"></div>
  <div class="back__stripe back__stripe--b"></div>
</section>

<section class="card card--front" aria-label="Card front">
  <div class="front__rule front__rule--top-a"></div>
  <div class="front__rule front__rule--top-b"></div>

  <div class="person">
    <p class="person__name">YOUR NAME HERE</p>
    <p class="person__title">YOUR TITLE</p>
  </div>

  <ul class="contact">
    <li class="contact__item">
      <span class="icon"><svg width="12" height="12" viewBox="0 0 12 12"><path d="M6 1 1 5.5h1.5V11h2.5V8h2v3h2.5V5.5H11z" fill="#fff"/></svg></span>
      123 Main St, Anywhere, ST 12345
    </li>
    <li class="contact__item contact__item--phone">
      <span class="icon"><svg width="12" height="12" viewBox="0 0 12 12"><rect x="3.5" y="1" width="5" height="10" rx="1" fill="#fff"/><rect x="4.5" y="2.2" width="3" height="6" fill="#5cc21c"/></svg></span>
      123-456-7890
    </li>
    <li class="contact__item">
      <span class="icon"><svg width="12" height="12" viewBox="0 0 12 12"><rect x="1.5" y="3" width="9" height="6.5" fill="#fff"/><path d="M1.5 3 6 7l4.5-4" fill="none" stroke="#5cc21c" stroke-width="1"/></svg></span>
      email@yourwebsite.com
    </li>
  </ul>

  <div class="wordmark front__logo"><span class="wordmark__square"></span>Torvelin</div>

  <div class="website">
    www.yourwebsite.com
    <span class="icon"><svg width="12" height="12" viewBox="0 0 12 12"><circle cx="6" cy="6" r="4.5" fill="none" stroke="#fff" stroke-width="1.2"/><path d="M1.5 6h9M6 1.5c-2 2.5-2 6.5 0 9M6 1.5c2 2.5 2 6.5 0 9" fill="none" stroke="#fff" stroke-width="1"/></svg></span>
  </div>

  <div class="front__rule front__rule--bottom-a"></div>
  <div class="front__rule front__rule--bottom-b"></div>
</section>

</body>
</html>
```